Packaging Tape Design for Retail / Ecommerce Company

We need a design for custom packing tape for our company. We would like to see two designs for the packaging tape. 1) with the word fragile attached 2) Similiar design without the fragileMinimum resolution is 300 .ppi 3" x 6" or 3" x 12" - If selected, request that font that are used be identified. Orla Hearth Logo and package - Nest Bright! is a tagline we use on documents and correspondence. Looking for a creative design.

Target Market(s)

Mid level to high end consumers

Industry/Entity Type

Retail

Font styles to use
Sans Serif

Requirements
Must have
• logo must be included
• Nest Bright! - must be included
• web address: orlahearth.com
Nice to have
• creativity

```html
<!DOCTYPE html>
<html lang="en">
<head>
<meta charset="utf-8">
<title>Orla Hearth Packing Tape</title>
<link rel="stylesheet" href="https://fonts.googleapis.com/css2?family=Montserrat:wght@600;800&family=Allura&display=swap">
<style>
  :root {
    --tape-cream: #dcd8b2;
    --brand-red: #7b1f0c;
    --backdrop: #e4e4e2;
    --band-width: 38px;
  }
  * { margin: 0; padding: 0; box-sizing: border-box; }
  html, body {
    width: 1200px;
    height: 900px;
    overflow: hidden;
    background: var(--backdrop);
  }
  .canvas {
    position: relative;
    width: 1200px;
    height: 900px;
    display: flex;
    align-items: center;
  }
  .tape-strip {
    display: flex;
    width: 1200px;
    height: 320px;
    background: var(--tape-cream);
    overflow: hidden;
  }
  .tape-unit {
    position: relative;
    flex: 0 0 240px;
    height: 100%;
  }
  .unit-frame {
    position: absolute;
    left: 0;
    top: 0;
    width: 240px;
    height: 320px;
  }
  .unit-frame path {
    fill: none;
    stroke: var(--brand-red);
    stroke-width: 2.5;
  }
  .brand-band {
    position: absolute;
    left: 100px;
    top: 0;
    width: var(--band-width);
    height: 100%;
    background: var(--brand-red);
  }
  .vertical-text {
    position: absolute;
    top: 0;
    height: 100%;
    display: flex;
    align-items: center;
    justify-content: center;
    writing-mode: vertical-rl;
    transform: rotate(180deg);
    color: var(--brand-red);
    white-space: nowrap;
  }
  .brand-name {
    left: 50px;
    width: 44px;
    font-family: "Montserrat", sans-serif;
    font-weight: 800;
    font-size: 28px;
    letter-spacing: 0.5px;
  }
  .tagline {
    left: 142px;
    width: 52px;
    font-family: "Allura", cursive;
    font-size: 50px;
  }
  .web-address {
    left: 196px;
    width: 22px;
    font-family: "Montserrat", sans-serif;
    font-weight: 600;
    font-size: 15px;
  }
</style>
</head>
<body>
<main class="canvas">
  <section class="tape-strip" aria-label="Orla Hearth packing tape pattern">
    <div class="tape-unit">
      <svg class="unit-frame" viewBox="0 0 240 320" aria-hidden="true"><path d="M110 42 H52 Q10 160 52 278 H110"/></svg>
      <div class="brand-band"></div>
      <p class="vertical-text brand-name">Orla Hearth</p>
      <p class="vertical-text tagline">Nest Bright!</p>
      <p class="vertical-text web-address">orlahearth.com</p>
    </div>
    <div class="tape-unit">
      <svg class="unit-frame" viewBox="0 0 240 320" aria-hidden="true"><path d="M110 42 H52 Q10 160 52 278 H110"/></svg>
      <div class="brand-band"></div>
      <p class="vertical-text brand-name">Orla Hearth</p>
      <p class="vertical-text tagline">Nest Bright!</p>
      <p class="vertical-text web-address">orlahearth.com</p>
    </div>
    <div class="tape-unit">
      <svg class="unit-frame" viewBox="0 0 240 320" aria-hidden="true"><path d="M110 42 H52 Q10 160 52 278 H110"/></svg>
      <div class="brand-band"></div>
      <p class="vertical-text brand-name">Orla Hearth</p>
      <p class="vertical-text tagline">Nest Bright!</p>
      <p class="vertical-text web-address">orlahearth.com</p>
    </div>
    <div class="tape-unit">
      <svg class="unit-frame" viewBox="0 0 240 320" aria-hidden="true"><path d="M110 42 H52 Q10 160 52 278 H110"/></svg>
      <div class="brand-band"></div>
      <p class="vertical-text brand-name">Orla Hearth</p>
      <p class="vertical-text tagline">Nest Bright!</p>
      <p class="vertical-text web-address">orlahearth.com</p>
    </div>
    <div class="tape-unit">
      <svg class="unit-frame" viewBox="0 0 240 320" aria-hidden="true"><path d="M110 42 H52 Q10 160 52 278 H110"/></svg>
      <div class="brand-band"></div>
      <p class="vertical-text brand-name">Orla Hearth</p>
      <p class="vertical-text tagline">Nest Bright!</p>
      <p class="vertical-text web-address">orlahearth.com</p>
    </div>
  </section>
</main>
</body>
</html>
```